I am looking for a design for my business card. I need a logo. The company is called Harborline Capital. We are an investment management and technology consulting company. I am looking for a professional conservative design. I think a lighthouse might be a good simple for us.

For the business card.
company URL www.harborlinecapital.example
my name: Philip R. Kessler
email: pkessler@harborlinecapital.example
my phone # 318-469-5730

Contact Information for Business Card

company URL www.harborlinecapital.example my name: Philip R. Kessler email: pkessler@harborlinecapital.example my phone # 318-469-5730

Colors
0054AA
0677BA
7BADD7
CADEEF
E8F1F8

Requirements
Must have
• area on the back for a QR code

```html
<!DOCTYPE html>
<html lang="en">
<head>
<meta charset="utf-8">
<title>Harborline Capital — Business Card</title>
<link rel="stylesheet" href="https://fonts.googleapis.com/css2?family=Montserrat:wght@400;500;700&display=swap">
<style>
  :root {
    --navy: #083d6f;
    --gold: #f0bf2c;
    --white: #ffffff;
    --backdrop: #3b3b3c;
  }
  * { margin: 0; padding: 0; box-sizing: border-box; }
  html, body {
    width: 1200px;
    height: 1200px;
    overflow: hidden;
    background: var(--backdrop);
    font-family: "Montserrat", Arial, sans-serif;
  }
  .card {
    position: absolute;
    left: 180px;
    width: 840px;
    height: 480px;
    border-radius: 34px;
    overflow: hidden;
    background: var(--navy);
  }
  .card-front { top: 90px; }
  .card-back  { top: 630px; }

  .front-shape {
    position: absolute;
    inset: 0;
    width: 100%;
    height: 100%;
  }

  .wordmark {
    position: absolute;
    font-weight: 700;
    letter-spacing: 0.08em;
    text-transform: uppercase;
    text-align: center;
    line-height: 1.15;
  }
  .front-wordmark {
    left: 450px;
    top: 150px;
    width: 370px;
    font-size: 34px;
    color: var(--navy);
  }
  .back-wordmark {
    left: 0;
    right: 0;
    top: 180px;
    font-size: 48px;
    color: var(--white);
  }

  .qr-area {
    position: absolute;
    right: 48px;
    bottom: 44px;
    width: 96px;
    height: 96px;
    border-radius: 8px;
    background: var(--white);
  }

  .contact {
    position: absolute;
    left: 56px;
    top: 240px;
    color: var(--white);
  }
  .contact-name {
    font-size: 26px;
    font-weight: 700;
    color: var(--gold);
    text-transform: uppercase;
    letter-spacing: 0.01em;
  }
  .contact-title {
    font-size: 20px;
    font-weight: 500;
    margin-bottom: 14px;
  }
  .contact-line {
    display: flex;
    align-items: center;
    gap: 12px;
    font-size: 16px;
    font-weight: 400;
    margin-top: 8px;
  }
  .contact-icon {
    width: 22px;
    height: 22px;
    flex: none;
    fill: none;
    stroke: var(--gold);
    stroke-width: 2;
  }
  .contact-icon .solid { fill: var(--gold); stroke: none; }
</style>
</head>
<body>

<section class="card card-front">
  <svg class="front-shape" viewBox="0 0 840 480" aria-hidden="true">
    <path d="M360 0 L840 0 L840 480 L710 480 C480 465 375 300 360 0 Z" fill="var(--white)"/>
    <path d="M372 0 C388 290 490 458 716 480" fill="none" stroke="var(--gold)" stroke-width="9"/>
  </svg>

  <div class="wordmark front-wordmark">Harborline<br>Capital</div>

  <div class="contact">
    <div class="contact-name">Philip R. Kessler</div>
    <div class="contact-title">CEO</div>
    <div class="contact-line">
      <svg class="contact-icon" viewBox="0 0 24 24"><path class="solid" d="M6.6 10.8a15 15 0 0 0 6.6 6.6l2.2-2.2a1 1 0 0 1 1-.25 11.4 11.4 0 0 0 3.6.57 1 1 0 0 1 1 1V20a1 1 0 0 1-1 1A17 17 0 0 1 3 4a1 1 0 0 1 1-1h3.5a1 1 0 0 1 1 1c0 1.25.2 2.45.57 3.57a1 1 0 0 1-.25 1z"/></svg>
      <span>318-469-5730</span>
    </div>
    <div class="contact-line">
      <svg class="contact-icon" viewBox="0 0 24 24"><rect x="3" y="6" width="18" height="12"/><path d="M3 6l9 7 9-7M3 18l7-6M21 18l-7-6"/></svg>
      <span>pkessler@harborlinecapital.example</span>
    </div>
    <div class="contact-line">
      <svg class="contact-icon" viewBox="0 0 24 24"><circle cx="12" cy="12" r="9"/><ellipse cx="12" cy="12" rx="4" ry="9"/><path d="M3 12h18M5 7.5h14M5 16.5h14"/></svg>
      <span>www.harborlinecapital.example</span>
    </div>
  </div>
</section>

<section class="card card-back">
  <div class="wordmark back-wordmark">Harborline<br>Capital</div>
  <div class="qr-area" role="img" aria-label="Reserved space for QR code"></div>
</section>

</body>
</html>
```